Minimalist Modern Business Card Design, open to ideas, or cleaner version of provided files, but what logo & logo colors (with some black) as shown in files, and info for back shown in files as well.

```html
<!DOCTYPE html>
<html lang="en">
<head>
<meta charset="utf-8">
<title>Wayside Fleet Works – Business Card</title>
<link rel="stylesheet" href="https://fonts.googleapis.com/css2?family=Montserrat:ital,wght@0,400;0,500;0,600;0,700;1,400&display=swap">
<style>
  :root {
    --navy: #2a2768;
    --ink: #1d1d24;
    --card: #ffffff;
    --backdrop: #d6d6d6;
  }
  * { box-sizing: border-box; margin: 0; padding: 0; }
  html, body {
    width: 1200px; height: 896px; overflow: hidden;
    background: var(--backdrop);
    font-family: "Montserrat", sans-serif;
  }
  .card {
    position: absolute; left: 334px; width: 528px; height: 300px;
    background: var(--card); border-radius: 28px;
    box-shadow: 0 10px 22px rgba(0,0,0,0.18);
  }
  .card--front { top: 126px; }
  .card--back { top: 475px; }

  .brand {
    position: absolute; left: 33px; top: 112px;
    display: flex; align-items: center; gap: 16px;
  }
  .brand__square { width: 34px; height: 34px; background: var(--navy); }
  .brand__name {
    color: var(--navy); font-weight: 600; font-size: 27px; line-height: 1.0;
  }
  .divider {
    position: absolute; left: 305px; top: 100px; width: 1.5px; height: 101px;
    background: var(--navy);
  }
  .contact { position: absolute; left: 329px; top: 88px; color: var(--ink); }
  .contact__name { color: var(--navy); font-weight: 700; font-size: 21px; letter-spacing: 0.2px; line-height: 1.1; }
  .contact__role { font-style: italic; font-size: 14.5px; margin-top: 1px; }
  .contact__line { font-size: 14.5px; margin-top: 10px; }
  .contact__role + .contact__line { margin-top: 20px; }
  .contact__label { font-weight: 700; }

  .list { position: absolute; top: 26px; color: var(--ink); }
  .list--services { left: 36px; }
  .list--makes { left: 331px; }
  .list__title { font-weight: 700; font-size: 13.5px; margin-bottom: 7px; }
  .list__item {
    display: flex; align-items: center; gap: 10px;
    font-size: 12.8px; height: 23px;
  }
  .list--makes .list__item { gap: 14px; }
  .list--makes .list__title { margin-bottom: 9px; }
  .list__bullet {
    width: 9.5px; height: 9.5px; background: var(--navy);
    transform: rotate(45deg); flex: none;
  }
</style>
</head>
<body>
  <section class="card card--front">
    <div class="brand">
      <span class="brand__square"></span>
      <span class="brand__name">Wayside<br>Fleet Works</span>
    </div>
    <div class="divider"></div>
    <div class="contact">
      <p class="contact__name">DANIEL HARPER</p>
      <p class="contact__role">Managing Director</p>
      <p class="contact__line"><span class="contact__label">M:</span> 555 210 487</p>
      <p class="contact__line"><span class="contact__label">E:</span> hello@wayside.co</p>
    </div>
  </section>

  <section class="card card--back">
    <div class="list list--services">
      <p class="list__title">SERVICES INCLUDE:</p>
      <p class="list__item"><span class="list__bullet"></span>Shop &amp; Mobile</p>
      <p class="list__item"><span class="list__bullet"></span>DOT &amp; BIT Inspeections</p>
      <p class="list__item"><span class="list__bullet"></span>All Maintenance &amp; Repairs</p>
      <p class="list__item"><span class="list__bullet"></span>Check Engine Lights</p>
      <p class="list__item"><span class="list__bullet"></span>Diags, Regens &amp; Programming</p>
      <p class="list__item"><span class="list__bullet"></span>Full Dealer Software Capabilities</p>
      <p class="list__item"><span class="list__bullet"></span>PM &amp; Compliance Tracking</p>
      <p class="list__item"><span class="list__bullet"></span>App-Based Billing &amp; Live Updates</p>
      <p class="list__item"><span class="list__bullet"></span>Dealer Certified Techs</p>
      <p class="list__item"><span class="list__bullet"></span>Night Servicing to Avoid Downtime</p>
    </div>
    <div class="list list--makes">
      <p class="list__title">SPECIALIZING IN:</p>
      <p class="list__item"><span class="list__bullet"></span>Heavy &amp; Medium Duty</p>
      <p class="list__item"><span class="list__bullet"></span>Corvane</p>
      <p class="list__item"><span class="list__bullet"></span>Ikora</p>
      <p class="list__item"><span class="list__bullet"></span>Havel</p>
      <p class="list__item"><span class="list__bullet"></span>Pellmark</p>
      <p class="list__item"><span class="list__bullet"></span>Fairhaul</p>
      <p class="list__item"><span class="list__bullet"></span>Kestline</p>
      <p class="list__item"><span class="list__bullet"></span>Arlen</p>
      <p class="list__item"><span class="list__bullet"></span>After Treatment</p>
      <p class="list__item"><span class="list__bullet"></span>And More</p>
    </div>
  </section>
</body>
</html>
```